Vessa Almond Protein - Less, but better

Design a protein powder pouch (350g). Take inspiration from Brimora.co and put the same information on the pouch and add "made in Australia". I do not want it to be exactly the same design but just take some inspiration from it.

```html
<!DOCTYPE html>
<html lang="en">
<head>
<meta charset="utf-8">
<title>Vessa Almond Protein – Pouch Label</title>
<link rel="stylesheet" href="https://fonts.googleapis.com/css2?family=Fredoka:wght@400;500;600;700&display=swap">
<style>
  :root {
    --bg-green: #2a8c68;
    --forest: #1f3a30;
    --cream: #f7f2e6;
    --sage: #7a9e8e;
    --blush: #e8a9a3;
    --amber: #f0a500;
  }
  html, body {
    margin: 0;
    padding: 0;
    width: 1200px;
    height: 849px;
    overflow: hidden;
    background: var(--bg-green);
    font-family: "Fredoka", sans-serif;
  }
  .stage {
    position: relative;
    width: 1200px;
    height: 849px;
  }
  .pouch-label {
    position: absolute;
    left: 360px;
    top: 90px;
    width: 480px;
    height: 669px;
    display: block;
  }
  .brand-name { font-family: "Fredoka", sans-serif; font-weight: 600; font-size: 46px; fill: var(--cream); letter-spacing: 10px; }
  .badge-ring-text { font-family: "Fredoka", sans-serif; font-weight: 600; font-size: 18px; fill: var(--cream); letter-spacing: 0.5px; }
  .product-name { font-family: "Fredoka", sans-serif; font-weight: 600; font-size: 27px; fill: var(--forest); letter-spacing: 0.5px; }
  .origin-note { font-family: "Fredoka", sans-serif; font-weight: 600; font-size: 8.5px; fill: var(--cream); letter-spacing: 0.3px; }
  .health-claim { font-family: "Fredoka", sans-serif; font-weight: 600; font-size: 17px; fill: var(--cream); letter-spacing: 0.3px; }
  .benefit-list { font-family: "Fredoka", sans-serif; font-weight: 600; font-size: 9.5px; letter-spacing: 0.3px; }
  .benefit-heart, .benefit-hair { fill: var(--blush); }
  .benefit-digestion, .benefit-bone { fill: var(--cream); }
  .benefit-immune { fill: var(--sage); }
  .benefit-skin { fill: var(--amber); }
  .net-weight { font-family: "Fredoka", sans-serif; font-weight: 600; font-size: 8.5px; fill: var(--cream); letter-spacing: 0.3px; }
</style>
</head>
<body>
<main class="stage">
  <svg class="pouch-label" viewBox="0 0 480 669" xmlns="http://www.w3.org/2000/svg">
    <defs>
      <linearGradient id="artwork-tones" x1="0" y1="0" x2="1" y2="1">
        <stop offset="0" stop-color="#f0a500"/>
        <stop offset="0.25" stop-color="#f7f2e6"/>
        <stop offset="0.5" stop-color="#7a9e8e"/>
        <stop offset="0.75" stop-color="#e8a9a3"/>
        <stop offset="1" stop-color="#f7f2e6"/>
      </linearGradient>
      <path id="ring-top" d="M 134 398 A 106 106 0 0 1 346 398"/>
      <path id="ring-bottom" d="M 127.2 357 A 120 120 0 1 0 352.8 357"/>
    </defs>

    <rect class="top-band" x="0" y="0" width="480" height="200" fill="var(--forest)"/>

    <rect class="artwork-field" x="0" y="192" width="480" height="400" fill="url(#artwork-tones)"
          role="img" aria-label="Abstract flowing shapes in amber, sage, blush and cream"/>

    <path class="bottom-band" d="M 0 572 Q 240 546 480 572 L 480 669 L 0 669 Z" fill="var(--forest)"/>

    <text class="brand-name" x="245" y="118" text-anchor="middle">VESSA</text>

    <g class="product-badge">
      <circle cx="240" cy="398" r="130" fill="var(--forest)"/>
      <circle cx="240" cy="398" r="96" fill="var(--cream)"/>
      <text class="badge-ring-text" text-anchor="middle">
        <textPath href="#ring-top" startOffset="50%">REAL CHOCOLATE</textPath>
      </text>
      <text class="badge-ring-text" text-anchor="middle">
        <textPath href="#ring-bottom" startOffset="13%">VEGAN</textPath>
      </text>
      <text class="badge-ring-text" text-anchor="middle">
        <textPath href="#ring-bottom" startOffset="50%">JUST 4 INGREDIENTS</textPath>
      </text>
      <text class="badge-ring-text" text-anchor="middle">
        <textPath href="#ring-bottom" startOffset="86%">DELICIOUS</textPath>
      </text>
      <text class="product-name" x="240" y="372" text-anchor="middle">ALMOND</text>
      <text class="product-name" x="240" y="405" text-anchor="middle">PROTEIN</text>
      <text class="product-name" x="240" y="438" text-anchor="middle">POWDER</text>
    </g>

    <text class="origin-note" x="240" y="590" text-anchor="middle">MADE IN AUSTRALIA</text>
    <text class="health-claim" x="240" y="616" text-anchor="middle">NATURALLY SUPPORTS HEALTH</text>
    <text class="benefit-list" x="240" y="633" text-anchor="middle">
      <tspan class="benefit-heart">HEART</tspan>
      <tspan class="benefit-digestion">DIGESTION</tspan>
      <tspan class="benefit-immune">IMMUNE SYSTEM</tspan>
      <tspan class="benefit-skin">SKIN</tspan>
      <tspan class="benefit-bone">BONE</tspan>
      <tspan class="benefit-hair">HAIR</tspan>
    </text>
    <text class="net-weight" x="240" y="654" text-anchor="middle">NET WT 350G</text>
  </svg>
</main>
</body>
</html>
```